Motivational Quotes Poster Series

This is a 3 poster design series for Ridgeway Haul Academy. The size of each poster should be 18 inches wide and 24 inches tall. The goal of these posters is to serve as motivational "signs" to be hung in the office area for the employees (not customers). These employees are instructors/teachers, teaching students how to drive semi trucks. While each design is a separate poster and design, we're posting as 1 project because we'd like some continuity between the series. Below we'll break down the details of all 3 posters...

Poster #1
Text that must appear on poster - "If You Want The Best Out Of Each Student" and "Give The Best Of You!" Note: While this text must appear on the poster, you can arrange in the layout as you see fit. For example, first line could be at top of poster and second line on bottom.

Poster #2
Text that must appear on poster - "Invest In People" and "Change Someone's Life" (same notes apply as in 1st poster)

Poster #3
Text that must appear on poster - "Today Is..." and "Just Another Day For You" and "The Most Important Day In Their Life" Note: This can be laid out on the poster however you see fit, but each phrase needs to be separate and it needs to flow.

Target Market(s)

Truck Driver Training Instructors - These are middle-aged, mostly male, masculine type personalities.

Industry/Entity Type

Training

Requirements
Must have
• Must have noted text from description
Must have working files (ie - PSD, EPS, AI, etc) provided
Must have common theme between each poster in series
Must have easy to read font and layout
Must have product dimensions of 18 inches (width) by 24 inches (height). If design uses full dimensions please include quarter inch bleed.
Nice to have
• Nice to have a trucking theme...related to trucking industry, but not over the top. Example - This could mean subtle injection of background tire tracks, but by no means are tire tracks required.

For inspiration, you can visit the site at http://www.ridgewayhaulacademy.com. While you can use the colors of the site/logo, you can still branch out between each poster to try new colors within reason.

Note: While we've attached the logo to this project, it COULD be used but doesn't HAVE to be included in the design. The logo IS NOT a focal point. The phrases in the poster ARE the focal point.

```html
<!DOCTYPE html>
<html lang="en">
<head>
<meta charset="utf-8">
<title>Ridgeway Haul Academy — Motivational Poster Series</title>
<link href="https://fonts.googleapis.com/css2?family=Arvo:wght@700&display=swap" rel="stylesheet">
<style>
  :root {
    --stage: #ffffff;
    --poster-bg: #000000;
    --ink-white: #ffffff;
    --accent-red: #d3222a;
    --accent-orange: #f0923a;
    --accent-blue: #5aa6dc;
    --panel-maroon: #1e0806;
  }
  html, body {
    margin: 0;
    padding: 0;
    width: 1200px;
    height: 720px;
    overflow: hidden;
    background: var(--stage);
  }
  .series {
    position: relative;
    width: 1200px;
    height: 720px;
  }
  .poster {
    position: absolute;
    top: 100px;
    width: 272px;
    height: 362px;
    background: var(--poster-bg);
    overflow: hidden;
    font-family: "Arvo", "Rockwell", serif;
    font-weight: 700;
    color: var(--ink-white);
  }
  .poster--invest { left: 92px; }
  .poster--best { left: 469px; }
  .poster--today { left: 835px; }

  .truck-art {
    position: absolute;
    display: block;
  }
  .line {
    position: absolute;
    margin: 0;
    line-height: 1;
    white-space: nowrap;
  }
  .line--big { font-size: 34px; letter-spacing: 0.2px; }
  .line--mid { font-size: 23px; }
  .line--small { font-size: 13px; }
  .right { right: 14px; text-align: right; }

  .red { color: var(--accent-red); }
  .orange { color: var(--accent-orange); }
  .blue { color: var(--accent-blue); }

  .brand {
    position: absolute;
    display: flex;
    align-items: center;
    gap: 4px;
    font-size: 7px;
    line-height: 1;
    color: var(--ink-white);
  }
  .brand__dot {
    width: 8px;
    height: 8px;
    border-radius: 50%;
    background: var(--ink-white);
  }
</style>
</head>
<body>
<main class="series">

  <!-- Poster: Invest in People -->
  <section class="poster poster--invest">
    <svg class="truck-art" style="left:0; top:100px" width="190" height="262" role="img" aria-label="Grey wireframe drawing of a semi truck cab, front three-quarter view">
      <defs>
        <radialGradient id="greyTruck" cx="50%" cy="60%" r="60%">
          <stop offset="0" stop-color="#8a8a8a" stop-opacity="0.75"/>
          <stop offset="1" stop-color="#000000" stop-opacity="0"/>
        </radialGradient>
      </defs>
      <rect width="190" height="262" fill="url(#greyTruck)"/>
    </svg>
    <p class="line line--big right" style="top:26px">Invest</p>
    <p class="line line--small right" style="top:62px">In People</p>
    <p class="line line--big right red" style="top:76px">Change</p>
    <p class="line line--small right" style="top:113px">Someone's</p>
    <p class="line line--big right" style="top:134px">Life</p>
    <div class="brand" style="right:14px; bottom:10px">
      <span class="brand__dot"></span><span>Ridgeway Haul Academy</span>
    </div>
  </section>

  <!-- Poster: Give the Best -->
  <section class="poster poster--best">
    <svg class="truck-art" style="left:0; top:0" width="272" height="362" aria-hidden="true">
      <rect x="60" y="60" width="260" height="270" fill="var(--panel-maroon)" transform="rotate(-22 190 195)"/>
    </svg>
    <svg class="truck-art" style="left:88px; top:70px" width="184" height="245" role="img" aria-label="Orange glowing wireframe drawing of a semi truck cab">
      <defs>
        <radialGradient id="orangeTruck" cx="45%" cy="60%" r="60%">
          <stop offset="0" stop-color="#e8862e" stop-opacity="0.8"/>
          <stop offset="1" stop-color="#1e0806" stop-opacity="0"/>
        </radialGradient>
      </defs>
      <rect width="184" height="245" fill="url(#orangeTruck)"/>
    </svg>
    <p class="line line--small" style="left:11px; top:27px">You</p>
    <p class="line line--mid orange" style="left:11px; top:45px">Want The Best</p>
    <p class="line line--small" style="left:11px; top:72px">Out Of Each</p>
    <p class="line line--small" style="left:11px; top:90px">Student...</p>
    <p class="line line--mid orange" style="left:14px; top:305px">Give The Best</p>
    <p class="line line--small" style="left:14px; top:332px">Of You!</p>
    <div class="brand" style="right:14px; bottom:12px">
      <span class="brand__dot"></span><span>Ridgeway Haul Academy</span>
    </div>
  </section>

  <!-- Poster: Today Is -->
  <section class="poster poster--today">
    <svg class="truck-art" style="left:0; top:60px" width="200" height="240" role="img" aria-label="Blue wireframe drawing of a semi truck cab, front view">
      <defs>
        <radialGradient id="blueTruck" cx="50%" cy="55%" r="60%">
          <stop offset="0" stop-color="#4f8fc4" stop-opacity="0.8"/>
          <stop offset="1" stop-color="#000000" stop-opacity="0"/>
        </radialGradient>
      </defs>
      <rect width="200" height="240" fill="url(#blueTruck)"/>
    </svg>
    <p class="line line--mid right blue" style="top:20px; font-size:27px">Today Is-</p>
    <p class="line line--small right" style="top:50px">Just Another Day For You</p>
    <p class="line line--small right" style="top:289px">The Most Important Day -</p>
    <p class="line right" style="top:304px; font-size:27px"><span style="font-size:13px">In</span><span class="blue">Their Life</span></p>
    <div class="brand" style="left:14px; bottom:12px">
      <span class="brand__dot"></span><span>Ridgeway Haul Academy</span>
    </div>
  </section>

</main>
</body>
</html>
```